Business cards design for T38 (Разработка визитных карточек)

We would like to get design of our business cards loosely based on our website design [url removed, login to view]

logo in vector is atteched

There should be following info to be present on business card:
Martin Colvey
CEO
T38
+7 (222) 222-22-22
+7 (222) 222-22-22
colvey@tessarine-mail.ru
222222, Moscow, Ulitsa Tikhvoronskaya, 7B

```html
<!DOCTYPE html>
<html lang="en">
<head>
<meta charset="utf-8">
<title>T38 business cards</title>
<link href="https://fonts.googleapis.com/css2?family=PT+Sans:wght@700&family=Tinos:wght@400&display=swap" rel="stylesheet">
<style>
  :root {
    --backdrop: #565656;
    --brand-red: #e60000;
    --paper: #ffffff;
    --ink: #1a1a1a;
  }
  * { box-sizing: border-box; margin: 0; padding: 0; }
  html, body {
    width: 1200px;
    height: 1005px;
    overflow: hidden;
    background: var(--backdrop);
  }
  .canvas {
    position: relative;
    width: 1200px;
    height: 1005px;
  }
  .card {
    position: absolute;
    top: 357px;
    width: 510px;
    height: 291px;
  }
  .card-front {
    left: 52px;
    background: var(--paper);
    border: 6px solid var(--brand-red);
  }
  .card-back {
    left: 638px;
    background: var(--brand-red);
    overflow: hidden;
  }
  .wordmark {
    font-family: "PT Sans", Arial, sans-serif;
    font-weight: 700;
    color: var(--brand-red);
    letter-spacing: 2px;
    line-height: 1;
  }
  .card-front .wordmark {
    position: absolute;
    left: 0;
    right: 0;
    top: 88px;
    text-align: center;
    font-size: 96px;
  }
  .site-address {
    position: absolute;
    right: 28px;
    bottom: 20px;
    font-family: "Tinos", "Times New Roman", serif;
    font-weight: 700;
    font-size: 14px;
    letter-spacing: 1.5px;
    color: var(--ink);
  }
  .site-address .site-brand { color: var(--brand-red); }
  .back-panel {
    position: absolute;
    left: 110px;
    top: 0;
    width: 290px;
    height: 291px;
    background: var(--paper);
  }
  .card-back .wordmark {
    position: absolute;
    left: 0;
    right: 0;
    top: 62px;
    text-align: center;
    font-size: 44px;
  }
  .holder-name {
    position: absolute;
    left: 188px;
    top: 172px;
    font-family: "Tinos", "Times New Roman", serif;
    font-size: 18px;
    color: var(--ink);
    white-space: nowrap;
  }
  .holder-role {
    font-size: 10px;
    color: var(--brand-red);
    margin-left: 4px;
  }
  .contact-list {
    position: absolute;
    left: 206px;
    top: 199px;
    list-style: none;
    font-family: "Tinos", "Times New Roman", serif;
    font-size: 10.5px;
    line-height: 12px;
    color: var(--ink);
  }
</style>
</head>
<body>
<main class="canvas">
  <section class="card card-front" aria-label="Business card front">
    <div class="wordmark">T38</div>
    <div class="site-address">www.<span class="site-brand">t38</span>project.ru</div>
  </section>

  <section class="card card-back" aria-label="Business card back">
    <div class="back-panel"></div>
    <div class="wordmark">T38</div>
    <p class="holder-name">Martin Colvey<span class="holder-role">CEO</span></p>
    <ul class="contact-list">
      <li>+7 (222) 222-22-22</li>
      <li>+7 (222) 222-22-22</li>
      <li>colvey@tessarine-mail.ru</li>
      <li>222222, Moscow,</li>
      <li>Ulitsa Tikhvoronskaya, 7B</li>
    </ul>
  </section>
</main>
</body>
</html>
```